Local Roofing/Construction company business needs new biz card design

We need a new business card design, current cards are from the start of this operation and generic at best. We are a local Construction Company (General Contractor) with a majority of our work originating from insurance claims-exterior finish work is the main focus (Roofs-Siding-Gutters etc). Heavily involved with homeowners and the low ball offers they receive from insurance company's after a insurable event takes place. I have attached some of our original logo file(s) below.

```html
<!DOCTYPE html>
<html lang="en">
<head>
<meta charset="utf-8">
<title>Stoneline Construction – Business Card</title>
<link rel="stylesheet" href="https://fonts.googleapis.com/css2?family=Montserrat:wght@400;500;700;800&display=swap">
<style>
  :root {
    --brand-green: #52b36a;
    --brand-green-dark: #4aa561;
    --ink: #2b2b2b;
    --ink-dark: #1c2b22;
    --card-white: #ffffff;
    --backdrop: #e6e8e6;
  }
  * { box-sizing: border-box; margin: 0; padding: 0; }
  html, body { width: 1200px; height: 900px; overflow: hidden; }
  body {
    background: var(--backdrop);
    font-family: "Montserrat", sans-serif;
    display: flex;
    flex-direction: column;
    align-items: center;
    justify-content: center;
    gap: 56px;
  }
  .card {
    position: relative;
    width: 640px;
    height: 366px;
    overflow: hidden;
    box-shadow: 0 6px 18px rgba(0,0,0,0.15);
  }

  /* Front */
  .card-front { background: var(--card-white); }
  .brand-name {
    position: absolute;
    top: 42px; left: 44px;
    display: flex; align-items: center; gap: 12px;
    color: var(--brand-green);
    font-weight: 800;
    font-size: 30px;
    letter-spacing: 1px;
    text-transform: uppercase;
    line-height: 1;
  }
  .brand-square { width: 26px; height: 26px; background: var(--brand-green); }
  .contact {
    position: absolute;
    top: 138px; left: 44px;
    color: var(--ink);
    font-size: 15px;
    font-weight: 400;
    line-height: 1.55;
    letter-spacing: 0.3px;
  }
  .contact-address { margin-bottom: 6px; }
  .contact-line { display: flex; align-items: center; gap: 8px; }
  .contact-line svg { width: 13px; height: 13px; flex: none; fill: var(--brand-green); }
  .person {
    position: absolute;
    top: 178px; right: 44px;
    text-align: right;
  }
  .person-name {
    color: var(--brand-green);
    font-weight: 700;
    font-size: 24px;
    letter-spacing: 2px;
    text-transform: uppercase;
  }
  .person-title {
    color: var(--ink);
    font-size: 15px;
    letter-spacing: 0.5px;
    margin-top: 2px;
  }
  .accent-bar {
    position: absolute;
    right: 0; top: 188px;
    width: 18px; height: 46px;
    background: var(--brand-green);
  }

  /* Back */
  .card-back { background: var(--brand-green); }
  .back-pattern {
    position: absolute; inset: 0;
    background: linear-gradient(135deg, var(--brand-green) 0%, var(--brand-green-dark) 100%);
  }
  .back-brand {
    position: absolute;
    right: 40px; bottom: 36px;
    display: flex; align-items: center; gap: 10px;
    color: var(--ink-dark);
    font-weight: 800;
    font-size: 22px;
    text-transform: uppercase;
    letter-spacing: 1px;
  }
  .back-brand .brand-square { width: 20px; height: 20px; background: var(--ink-dark); }
</style>
</head>
<body>
  <section class="card card-front">
    <div class="brand-name"><span class="brand-square"></span>Stoneline Construction</div>

    <div class="contact">
      <p class="contact-address">1480 W Harlan Avenue<br>Ridgeview County 5307</p>
      <p class="contact-line">
        <svg viewBox="0 0 24 24" aria-hidden="true"><path d="M6.6 10.8a15.1 15.1 0 0 0 6.6 6.6l2.2-2.2c.3-.3.7-.4 1-.2 1.1.4 2.3.6 3.6.6.6 0 1 .4 1 1V20c0 .6-.4 1-1 1A17 17 0 0 1 3 4c0-.6.4-1 1-1h3.5c.6 0 1 .4 1 1 0 1.3.2 2.5.6 3.6.1.3 0 .7-.2 1z"/></svg>
        0471 582 913
      </p>
      <p class="contact-line">
        <svg viewBox="0 0 24 24" aria-hidden="true"><path d="M2 5h20v14H2zm2 2v.5l8 5 8-5V7zm0 2.8V17h16V9.8l-8 5z"/></svg>
        info@stonelinebuild.com
      </p>
      <p class="contact-line">
        <svg viewBox="0 0 24 24" aria-hidden="true"><path d="M12 2a10 10 0 1 0 0 20 10 10 0 0 0 0-20zm6.9 6h-3a15 15 0 0 0-1.3-3.9A8 8 0 0 1 18.9 8zM12 4c.8 1.2 1.5 2.5 1.9 4h-3.8c.4-1.5 1.1-2.8 1.9-4zM4.3 14a8 8 0 0 1 0-4h3.4a16 16 0 0 0 0 4zm.8 2h3a15 15 0 0 0 1.3 3.9A8 8 0 0 1 5.1 16zm3-8h-3a8 8 0 0 1 4.3-3.9C8.9 5.3 8.4 6.6 8.1 8zM12 20c-.8-1.2-1.5-2.5-1.9-4h3.8c-.4 1.5-1.1 2.8-1.9 4zm2.3-6H9.7a14 14 0 0 1 0-4h4.6a14 14 0 0 1 0 4zm.3 5.9c.6-1.2 1-2.5 1.3-3.9h3a8 8 0 0 1-4.3 3.9zm1.7-5.9a16 16 0 0 0 0-4h3.4a8 8 0 0 1 0 4z"/></svg>
        www.stonelinebuild.com
      </p>
    </div>

    <div class="person">
      <p class="person-name">Marcus Hale</p>
      <p class="person-title">Managing Director</p>
    </div>
    <div class="accent-bar"></div>
  </section>

  <section class="card card-back">
    <div class="back-pattern" role="img" aria-label="Repeating tone-on-tone brand pattern in green"></div>
    <div class="back-brand"><span class="brand-square"></span>Stoneline Construction</div>
  </section>
</body>
</html>
```